Ridgefall Stoneworks Business card logo

We are a tile and natural stone installation company with an emphasis on high quality and design assistance. I prefer a black background with a graphic logo or maybe a photo that gives a feel of tile/natural stone. I like bold, but tasteful colors. Something to really catch the eye without being gaudy. The final design should convey expert quality and attention to detail.

Contact Information for Business Card

RIDGEFALL STONEWORKS Quality Design and Installation

Other font styles liked:
• Graviton, Illegal curves

Requirements
Must have
• Business card must be an eye-catcher, but tasteful.
• Information I need on the card:
• Business name and tagline
• Warren Pelsby, owner
• Phone: (xxx) xxx-xxxx
• Email
• Website

```html
<!DOCTYPE html>
<html lang="en">
<head>
<meta charset="utf-8">
<title>Ridgefall Stoneworks – Business Card</title>
<link rel="stylesheet" href="https://fonts.googleapis.com/css2?family=Righteous&family=Questrial&display=swap">
<style>
  :root {
    --night: #0b0d1a;
    --deep-navy: #15203f;
    --steel-blue: #34466e;
    --haze: #c9ccd8;
    --mist: #e6e7ee;
    --violet-dusk: #4a4566;
    --line: rgba(255, 255, 255, 0.75);
    --ink-light: #ffffff;
    --shadow: rgba(0, 0, 0, 0.85);
  }
  html, body {
    margin: 0;
    padding: 0;
    width: 1200px;
    height: 702px;
    overflow: hidden;
    background: var(--night);
  }
  .card {
    position: relative;
    width: 1200px;
    height: 702px;
    overflow: hidden;
    background: var(--night);
  }
  .card__backdrop {
    position: absolute;
    inset: 0;
    background:
      radial-gradient(ellipse 300px 200px at 860px 230px, rgba(230, 231, 238, 0.55), transparent 70%),
      radial-gradient(ellipse 340px 190px at 620px 470px, rgba(214, 216, 226, 0.6), transparent 70%),
      radial-gradient(ellipse 260px 170px at 340px 170px, rgba(190, 200, 216, 0.45), transparent 70%),
      radial-gradient(ellipse 280px 200px at 1050px 520px, rgba(160, 160, 190, 0.4), transparent 70%),
      radial-gradient(ellipse 360px 320px at 100px 300px, rgba(52, 70, 110, 0.9), transparent 75%),
      radial-gradient(ellipse 300px 260px at 1150px 160px, rgba(74, 69, 102, 0.8), transparent 75%),
      linear-gradient(160deg, var(--deep-navy) 0%, var(--night) 45%, var(--violet-dusk) 100%);
  }
  .card__lines {
    position: absolute;
    inset: 0;
  }
  .card__lines line {
    stroke: var(--line);
    stroke-width: 1;
  }
  .card__tagline {
    position: absolute;
    top: 68px;
    left: 641px;
    margin: 0;
    font-family: "Questrial", "Century Gothic", sans-serif;
    font-size: 28px;
    font-weight: 400;
    letter-spacing: 0.5px;
    color: var(--ink-light);
    white-space: nowrap;
  }
  .card__title {
    position: absolute;
    left: 0;
    top: 0;
  }
  .card__title text {
    font-family: "Righteous", "Arial Black", sans-serif;
    font-size: 98px;
    fill: var(--ink-light);
  }
</style>
</head>
<body>
<main class="card">
  <div class="card__backdrop" role="img" aria-label="Abstract background of overlapping translucent diamond shapes in navy, steel grey and soft violet"></div>

  <svg class="card__lines" width="1200" height="702" viewBox="0 0 1200 702" aria-hidden="true">
    <line x1="0" y1="250" x2="600" y2="560"/>
    <line x1="0" y1="430" x2="520" y2="702"/>
    <line x1="0" y1="640" x2="120" y2="702"/>
    <line x1="660" y1="560" x2="1200" y2="290"/>
    <line x1="820" y1="702" x2="1200" y2="510"/>
  </svg>

  <p class="card__tagline">Quality Design and Installation</p>

  <svg class="card__title" width="1200" height="702" viewBox="0 0 1200 702">
    <defs>
      <filter id="title-shadow" x="-5%" y="-30%" width="110%" height="160%">
        <feDropShadow dx="5" dy="5" stdDeviation="3" flood-color="#000" flood-opacity="0.85"/>
      </filter>
    </defs>
    <text x="97" y="387" textLength="1001" lengthAdjust="spacingAndGlyphs" filter="url(#title-shadow)">RIDGEFALL STONEWORKS</text>
  </svg>
</main>
</body>
</html>
```